Stationary Design Foundation Repair Business

We need business card and letterhead design for foundation repair business. Design must compliment the supplied logo. Font is eurostyle. please feel free to ask any questions. Also if we could incorporate the KTW file into the design, but keep the size of it small. Personal details are located in the stationary file.
Updates
I just uploaded a business card design that i like. Just so you guys know what my taste is. Is it possible to create something like this with my business card?
Target Market(s)
Home owners, Builders, Building surveyors, Insurance companies
Industry/Entity Type
Business
Other font styles liked:
- eurostile extended / bold
Look and feel

```html
<!DOCTYPE html>
<html lang="en">
<head>
<meta charset="utf-8">
<title>Deep Footing Stationery</title>
<link rel="stylesheet" href="https://fonts.googleapis.com/css2?family=Michroma&family=Exo+2:wght@400;600;700&display=swap">
<style>
:root{
  --bg:#6a6a6a;
  --paper:#ffffff;
  --red:#d1202a;
  --black:#111111;
  --ink:#1a1a1a;
  --grey-text:#cfcfcf;
  --badge:#8a8a8a;
}
*{box-sizing:border-box;margin:0;padding:0}
html,body{width:1200px;height:1000px;overflow:hidden;background:var(--bg);font-family:"Exo 2",sans-serif;color:var(--ink)}
.canvas{position:relative;width:1200px;height:1000px}
.sheet{position:absolute;background:var(--paper);overflow:hidden;box-shadow:0 2px 6px rgba(0,0,0,.35)}
.top-rule{position:absolute;left:0;right:0;top:0;height:8px;background:var(--red)}
.foot{position:absolute;left:0;right:0;bottom:0;background:var(--black);border-top:5px solid var(--red)}

.brand{position:absolute;display:flex;align-items:center;gap:8px}
.brand-mark{width:14px;height:14px;background:var(--red)}
.brand-name{font-family:"Michroma",sans-serif;font-weight:400;color:var(--black);letter-spacing:.5px;white-space:nowrap}
.tagline{position:absolute;font-family:"Exo 2",sans-serif;font-weight:700;color:var(--red);letter-spacing:1.4px;white-space:nowrap}
.abn{position:absolute;font-size:10.5px;white-space:nowrap}

.contacts{position:absolute;list-style:none;font-size:8.5px;line-height:10.5px}
.contacts li{display:flex;align-items:flex-start;gap:5px}
.contacts svg{flex:none;width:7px;height:7px;margin-top:2px}

.reg{position:absolute;display:flex;align-items:center;gap:5px}
.reg-badge{border-radius:50%;border:2px solid var(--badge);background:#eee}
.reg-text strong{display:block;font-family:"Exo 2",sans-serif;font-weight:700;line-height:1}
.reg-text span{display:block;font-weight:600;line-height:1.1}

/* letterhead */
.letterhead{left:35px;top:22px;width:603px;height:854px}
.letterhead .foot{height:25px}

/* envelope */
.envelope{left:480px;top:125px;width:670px;height:345px}
.envelope .foot{height:28px}

/* card back */
.card-back{left:739px;top:478px;width:382px;height:237px;background:var(--black)}
.card-back .person{position:absolute;left:212px;top:30px;font-family:"Michroma",sans-serif;font-size:13px;color:var(--red)}
.card-back .role{position:absolute;left:212px;top:51px;font-size:8px;color:#ddd}
.card-back .contacts{color:#e6e6e6}

/* card front */
.card-front{left:739px;top:735px;width:382px;height:237px}
.card-front .foot{height:82px;display:flex;align-items:center;justify-content:space-between;padding:0 32px 0 32px}
.card-front .abn{position:static;color:#fff;font-size:12px}
.card-front .reg{position:static;color:#fff}
</style>
</head>
<body>
<div class="canvas">

  <section class="sheet letterhead" aria-label="Letterhead">
    <div class="top-rule"></div>
    <div class="brand" style="left:40px;top:54px"><div class="brand-mark"></div><span class="brand-name" style="font-size:16px">DEEP FOOTING</span></div>
    <div class="tagline" style="left:62px;top:72px;font-size:6.5px">PROFESSIONAL UNDERPINNING SERVICES</div>
    <div class="abn" style="left:228px;top:84px">ABN: 12 345 678 901</div>
    <div class="reg" style="left:447px;top:23px">
      <div class="reg-badge" style="width:28px;height:28px"></div>
      <div class="reg-text"><strong style="font-size:12px">REGISTERED</strong><span style="font-size:8px">Building Practitioner</span></div>
    </div>
    <ul class="contacts" style="left:447px;top:59px">
      <li><svg viewBox="0 0 7 7"><rect width="7" height="7" rx="1" fill="#d1202a"/></svg>0400 218 645</li>
      <li><svg viewBox="0 0 7 7"><rect width="7" height="7" rx="1" fill="#d1202a"/></svg>info@deepfooting.com.au</li>
      <li><svg viewBox="0 0 7 7"><rect width="7" height="7" rx="1" fill="#d1202a"/></svg>www.deepfooting.com.au</li>
      <li><svg viewBox="0 0 7 7"><rect width="7" height="7" rx="1" fill="#d1202a"/></svg>7 Wattle Court Northvale<br>Vic 3999</li>
    </ul>
    <div class="foot"></div>
  </section>

  <section class="sheet envelope" aria-label="Envelope">
    <div class="top-rule"></div>
    <div class="brand" style="left:45px;top:78px"><div class="brand-mark"></div><span class="brand-name" style="font-size:17px">DEEP FOOTING</span></div>
    <div class="tagline" style="left:68px;top:98px;font-size:7px">PROFESSIONAL UNDERPINNING SERVICES</div>
    <div class="abn" style="left:248px;top:111px">ABN: 12 345 678 901</div>
    <ul class="contacts" style="left:48px;top:160px">
      <li><svg viewBox="0 0 7 7"><rect width="7" height="7" rx="1" fill="#d1202a"/></svg>0400 218 645</li>
      <li><svg viewBox="0 0 7 7"><rect width="7" height="7" rx="1" fill="#d1202a"/></svg>info@deepfooting.com.au</li>
      <li><svg viewBox="0 0 7 7"><rect width="7" height="7" rx="1" fill="#d1202a"/></svg>www.deepfooting.com.au</li>
      <li><svg viewBox="0 0 7 7"><rect width="7" height="7" rx="1" fill="#d1202a"/></svg>7 Wattle Court Northvale<br>Vic 3999</li>
    </ul>
    <div class="reg" style="left:56px;top:220px">
      <div class="reg-badge" style="width:30px;height:30px"></div>
      <div class="reg-text"><strong style="font-size:13px">REGISTERED</strong><span style="font-size:8px">Building Practitioner</span></div>
    </div>
    <div class="foot"></div>
  </section>

  <section class="sheet card-back" aria-label="Business card back">
    <div class="person">Marcus Hale</div>
    <div class="role">Proprietor</div>
    <ul class="contacts" style="left:212px;top:144px;font-size:8.5px;line-height:15px">
      <li><svg viewBox="0 0 7 7" style="margin-top:4px"><rect width="7" height="7" rx="1" fill="#e6e6e6"/></svg>0400 218 645</li>
      <li><svg viewBox="0 0 7 7" style="margin-top:4px"><rect width="7" height="7" rx="1" fill="#e6e6e6"/></svg>info@deepfooting.com.au</li>
      <li><svg viewBox="0 0 7 7" style="margin-top:4px"><rect width="7" height="7" rx="1" fill="#e6e6e6"/></svg>www.deepfooting.com.au</li>
      <li><svg viewBox="0 0 7 7" style="margin-top:4px"><rect width="7" height="7" rx="1" fill="#e6e6e6"/></svg><span style="line-height:11px;padding-top:2px">7 Wattle Court Northvale<br>Vic 3999</span></li>
    </ul>
  </section>

  <section class="sheet card-front" aria-label="Business card front">
    <div class="brand" style="left:32px;top:78px"><div class="brand-mark"></div><span class="brand-name" style="font-size:16px">DEEP FOOTING</span></div>
    <div class="tagline" style="left:54px;top:96px;font-size:6.5px">PROFESSIONAL UNDERPINNING SERVICES</div>
    <div class="foot">
      <div class="abn">ABN: 12 345 678 901</div>
      <div class="reg">
        <div class="reg-badge" style="width:42px;height:42px;background:#222"></div>
        <div class="reg-text"><strong style="font-size:15px">REGISTERED</strong><span style="font-size:10px">Building Practitioner</span></div>
      </div>
    </div>
  </section>

</div>
</body>
</html>
```